Brevik Fabrication - Business Card Design

We would like a dark (likely black) themed business card to be able to hand out to potential clients. We may list our services on the card or keep it clean. Unsure. Logo attached

```html
<!DOCTYPE html>
<html lang="en">
<head>
<meta charset="utf-8">
<title>Brevik Fabrication – Business Card</title>
<link rel="stylesheet" href="https://fonts.googleapis.com/css2?family=Oswald:wght@400;600&family=Open+Sans:wght@400;600&display=swap">
<style>
  :root {
    --canvas: #2a2b2e;
    --card: #141416;
    --card-edge: #1d1e21;
    --orange: #ee6a2c;
    --orange-deep: #d9531d;
    --blue: #3b8fd6;
    --muted: #3a3b40;
  }
  * { box-sizing: border-box; margin: 0; padding: 0; }
  html, body { width: 1200px; height: 900px; overflow: hidden; }
  body {
    background: var(--canvas);
    display: flex;
    flex-direction: column;
    align-items: center;
    justify-content: center;
    gap: 60px;
    font-family: "Open Sans", Arial, sans-serif;
  }
  .card {
    position: relative;
    width: 600px;
    height: 343px;
    background: radial-gradient(ellipse at 40% 30%, var(--card-edge), var(--card) 70%);
    border-radius: 18px;
    overflow: hidden;
    box-shadow: 0 10px 30px rgba(0,0,0,.45);
  }
  .card svg.bands { position: absolute; inset: 0; }

  /* Back: company side */
  .brand {
    position: absolute;
    top: 108px;
    left: 0; right: 0;
    text-align: center;
  }
  .brand-name {
    display: inline-flex;
    align-items: center;
    gap: 14px;
    font-family: "Oswald", sans-serif;
    font-weight: 600;
    font-size: 50px;
    letter-spacing: 2px;
    text-transform: uppercase;
    color: var(--blue);
    line-height: 1;
  }
  .brand-dot {
    width: 30px; height: 30px;
    border-radius: 50%;
    background: var(--orange);
  }
  .brand-sub {
    margin-top: 10px;
    display: flex;
    align-items: center;
    justify-content: center;
    gap: 12px;
    font-family: "Oswald", sans-serif;
    font-weight: 600;
    font-size: 20px;
    letter-spacing: 4px;
    color: var(--orange);
    text-transform: uppercase;
  }
  .brand-sub::before, .brand-sub::after {
    content: ""; width: 40px; height: 2px; background: var(--orange);
  }
  .tagline {
    margin-top: 22px;
    font-size: 11.5px;
    letter-spacing: 1px;
    text-transform: uppercase;
    color: var(--blue);
  }

  /* Front: contact side */
  .person { position: absolute; top: 46px; left: 44px; }
  .person-name {
    font-family: "Oswald", sans-serif;
    font-weight: 400;
    font-size: 30px;
    letter-spacing: 1px;
    text-transform: uppercase;
    line-height: 1;
  }
  .person-name .first { color: var(--blue); }
  .person-name .last { color: var(--orange); }
  .person-role {
    margin-top: 4px;
    font-size: 14px;
    letter-spacing: 1.5px;
    text-transform: uppercase;
    color: var(--blue);
  }
  .contact-list { list-style: none; margin-top: 22px; }
  .contact-list li {
    display: flex;
    align-items: flex-start;
    gap: 12px;
    font-size: 14px;
    color: var(--blue);
    line-height: 1.35;
    margin-bottom: 7px;
  }
  .contact-list svg { flex: none; margin-top: 1px; }
  .corner-shape { position: absolute; right: 0; bottom: 0; }
</style>
</head>
<body>

  <section class="card card-back" aria-label="Business card, company side">
    <svg class="bands" width="600" height="343" viewBox="0 0 600 343">
      <defs>
        <pattern id="hatch" width="6" height="6" patternUnits="userSpaceOnUse" patternTransform="rotate(45)">
          <rect width="6" height="6" fill="#1b1c1f"/>
          <rect width="2" height="6" fill="#2c2d31"/>
        </pattern>
      </defs>
      <polygon points="0,0 120,0 100,20 0,20" fill="var(--orange-deep)"/>
      <polygon points="0,20 100,20 90,30 0,30" fill="url(#hatch)"/>
      <polygon points="380,318 600,318 600,343 355,343" fill="var(--orange-deep)"/>
      <polygon points="395,306 600,306 600,318 380,318" fill="url(#hatch)"/>
    </svg>
    <div class="brand">
      <div class="brand-name"><span class="brand-dot"></span>Brevik</div>
      <div class="brand-sub">Fabrication Inc</div>
      <p class="tagline">Professional commercial HVAC systems, and other mechanical services</p>
    </div>
  </section>

  <section class="card card-front" aria-label="Business card, contact side">
    <div class="person">
      <h1 class="person-name"><span class="first">Daniel</span> <span class="last">Harper</span></h1>
      <p class="person-role">General Manager</p>
      <ul class="contact-list">
        <li>
          <svg width="16" height="16" viewBox="0 0 16 16"><circle cx="8" cy="8" r="7" fill="none" stroke="var(--orange)" stroke-width="1.3"/><path d="M5.5 4.5l1.2 1.8-.7.8c.5 1 1.2 1.7 2.2 2.2l.8-.7 1.8 1.2-.6 1.2c-2.6-.3-4.6-2.3-4.9-4.9z" fill="var(--orange)"/></svg>
          403-555-0184
        </li>
        <li>
          <svg width="16" height="16" viewBox="0 0 16 16"><circle cx="8" cy="8" r="7" fill="none" stroke="var(--orange)" stroke-width="1.3"/><rect x="4.5" y="5.5" width="7" height="5" fill="none" stroke="var(--orange)" stroke-width="1.1"/><path d="M4.5 5.5L8 8.3l3.5-2.8" fill="none" stroke="var(--orange)" stroke-width="1.1"/></svg>
          info@brevikfabrication.com
        </li>
        <li>
          <svg width="16" height="16" viewBox="0 0 16 16"><circle cx="8" cy="8" r="7" fill="none" stroke="var(--orange)" stroke-width="1.3"/><circle cx="8" cy="8" r="3.6" fill="none" stroke="var(--orange)" stroke-width="1.1"/><path d="M4.4 8h7.2M8 4.4v7.2" stroke="var(--orange)" stroke-width="1"/></svg>
          www.brevikfabrication.com
        </li>
        <li>
          <svg width="16" height="16" viewBox="0 0 16 16"><circle cx="8" cy="8" r="7" fill="none" stroke="var(--orange)" stroke-width="1.3"/><path d="M8 12s-3-3.2-3-5.2a3 3 0 016 0C11 8.8 8 12 8 12z" fill="var(--orange)"/><circle cx="8" cy="6.8" r="1" fill="var(--card)"/></svg>
          <span>1280 42 St NE, Calgary<br>AB T2E 4K7 Canada</span>
        </li>
      </ul>
    </div>
    <svg class="corner-shape" width="300" height="250" viewBox="0 0 300 250" aria-hidden="true">
      <circle cx="230" cy="210" r="170" fill="var(--orange)"/>
    </svg>
  </section>

</body>
</html>
```